Brochure Design Project

Need to create a brochure/product information material for a Therapy Product.

Please find attached the file:
- this has all the information for the product, if you for visual affect need to remove some of the content please ensure you don't remove key information.

please use these items or create your own level bar if you feel it needs to look different to match better.

Please ensure you use Coral Framing Logo and RVK Logo.

will need to fit on a A4 folded double sided brochure
Updates

Hi All,

please be aware that i have updated some text. i have attached a new updated version of the brief with the changed text in bold and underlined. there are three sections where i have added and made changes. please ensure you make these changes to your designs also. Thank you for your submissions they all look great so far. 

Target Market(s)

Community Services, Child Protection, Youth Work, Schools, At-Risk Youth Orangisations

Industry/Entity Type

Product

Requirements
Must have
• Must have core information provided, be visually appealing.

```html
<!DOCTYPE html>
<html lang="en">
<head>
<meta charset="utf-8">
<title>RVK – Reflection, Rewards and Badges</title>
<link rel="stylesheet" href="https://fonts.googleapis.com/css2?family=PT+Sans:wght@400;700&display=swap">
<style>
  :root {
    --paper: #ffffff;
    --ink: #1d1d1b;
    --bar-red: #d7141e;
    --bar-orange: #e9773a;
    --bar-sand: #f2c98a;
    --bar-lime: #c7cf6a;
    --bar-green: #5fae3b;
    --marker: #6b6b6b;
    --badge-grey: #a9aaac;
    --badge-orange: #ef8a1f;
    --badge-ring: #111111;
  }
  * { box-sizing: border-box; margin: 0; padding: 0; }
  html, body { width: 846px; height: 1200px; overflow: hidden; background: var(--paper); }
  body {
    position: relative;
    font-family: "PT Sans", sans-serif;
    color: var(--ink);
    font-size: 16.6px;
    line-height: 24.4px;
  }
  .page-copy {
    position: absolute;
    left: 70px;
    top: 72px;
    width: 698px;
  }
  .page-copy p { text-align: justify; margin-bottom: 24.4px; }
  .lead-in { font-weight: 700; }

  .level-bar {
    position: relative;
    width: 644px;
    height: 37px;
    margin: 14px 0 52px 29px;
    border-radius: 19px;
    background: linear-gradient(90deg, var(--bar-red) 0%, var(--bar-orange) 25%, var(--bar-sand) 52%, var(--bar-lime) 72%, var(--bar-green) 100%);
  }
  .level-marker {
    position: absolute;
    left: 325px;
    top: -5px;
    width: 8px;
    height: 47px;
    border-radius: 3px;
    background: var(--marker);
  }
  .level-readout {
    position: absolute;
    right: 14px;
    top: 11px;
    font-size: 11px;
    line-height: 14px;
    font-weight: 700;
    color: #3e6b24;
  }

  .badge-art {
    border-radius: 50%;
    border: 4px solid var(--badge-ring);
  }
  .badge-hammer {
    float: left;
    width: 134px;
    height: 134px;
    margin: 2px 25px 10px 0;
    background: var(--badge-grey);
  }
  .badge-car {
    float: right;
    width: 146px;
    height: 146px;
    margin: 2px -20px 8px 24px;
    background: var(--badge-orange);
  }
  .badges p { text-align: left; }

  .brand-mark {
    position: absolute;
    right: 26px;
    bottom: 26px;
    display: flex;
    align-items: center;
    gap: 8px;
    font-weight: 700;
    font-size: 40px;
    line-height: 1;
    color: var(--ink);
  }
  .brand-square { width: 14px; height: 14px; background: var(--ink); }
</style>
</head>
<body>
  <main class="page-copy">
    <p>These are based on the working agreement and are the daily reflections that use the experiential learning cycle (Barker, Jenner &amp; Kolby, 2002; Ringwood, 1999; Ringwood &amp; Gillard, 1995).</p>

    <p><span class="lead-in">The GM inputs the reflected experience point score out of 5 per criteria.</span> Honesty is encourages along with genuine reflection on the events of the day. The goal is to simply reflect on the day. This Reflection works of the premise of empowerment of the child/ young person evaluation of self and then the earning of rewards is positive reinforcement for the right behaviours. This reflective conversation between the Player and the GM need to be strength based.</p>

    <p>The points go towards rewards that can be redeemed at the end of each cycle (usually weekly). The player also gains Experience Points towards their Level Bar.</p>

    <p>Throughout the play period every 3-6 months a significant Real World Reward can be obtain if a certain Level cap is achieved.</p>

    <div class="level-bar" role="img" aria-label="Level bar showing 110 of 250 experience points">
      <span class="level-marker"></span>
      <span class="level-readout">110/250XP</span>
    </div>

    <p>Each week depending on how many points the player has earned they win the associated rewards with the points gained for the week. The player can change their reward when a new cycle starts. Rewards are budgeted against the points gained. If a player averages 35 they will get a much better reward than averaging 5.</p>

    <section class="badges">
      <div class="badge-art badge-hammer" role="img" aria-label="Round badge illustration of a hammer"></div>
      <p>RVK also provides a <strong>Badges System</strong>. The badge system allows for the players motivation around collection, achievement and social play.</p>
      <p><span class="badge-art badge-car" role="img" aria-label="Round badge illustration of an orange muscle car"></span>Some Badges also reward in Game items. The Challenges associated with earning Badges are for completing significant development achievement, educational/employment success and independent living skills being displayed.</p>
      <p>This intervention is about creating long-term change in behaviour and attitude. It is designed to be highly engaging to the young person and focuses on real growth and change in the individual.</p>
    </section>
  </main>

  <div class="brand-mark" aria-label="Coral Framing">
    <span class="brand-square"></span>
    <span>CF</span>
  </div>
</body>
</html>
```